Business Card and Stationary Design

After the successful redesign of our logo we are wanting to follow suite and create a new business card and stationary design!

New Logo is attached, information required on the business card should contain a mixture of the following but layout/arrangement is up to the designer.

Happy if the national provider number and abn are on the back, and happy for them to be smaller than the rest.

I am also happy to receive single sided or weird and wonderful designs.

Name
Title
National Provider Number 7291
ABN 53 219 864 317
Level 3, 42 Marlow Street
Brookfield NSW 2318
Ph: 1300 987 214
Mobile: 0432 785 619
name@ferngatebuild.com.au
www.ferngatebuild.com.au

Target Market(s)

Professionals, Peers, Students, Suppliers...

Industry/Entity Type

Construction

Contact Information for Business Card

Listed in project description

Font styles to use
Other font styles liked:
• Century Gothic

Colors
0455a3
3176b5
ffffff

Requirements
Must have
• Professional Design, same color scheme as our logo
Nice to have
• Something that sets our apart from everyone else would be fantastic, open to size and shape and layout options, as long as they present professionally.
• Open to raised/embossed text, alternative materials, custom sizes, clear material
Should not have
• The color orange

```html
<!DOCTYPE html>
<html lang="en">
<head>
<meta charset="utf-8">
<title>Ferngatebuild Stationery</title>
<link rel="stylesheet" href="https://fonts.googleapis.com/css2?family=Questrial&family=Roboto:wght@400;700&display=swap">
<style>
  :root {
    --navy: #1f3a7a;
    --navy-dark: #15285a;
    --ink: #3a3a3a;
    --muted: #555;
    --paper: #f7f7f7;
    --white: #ffffff;
    --stage: #dcdcdc;
    --card: #e9ebee;
    --rule: #8a8f99;
  }
  * { box-sizing: border-box; margin: 0; padding: 0; }
  html, body { width: 1200px; height: 877px; overflow: hidden; }
  body { background: var(--stage); font-family: "Questrial", sans-serif; color: var(--ink); position: relative; }

  .brand { position: absolute; display: flex; align-items: center; gap: 5px; color: var(--navy); font-family: "Questrial", sans-serif; line-height: 1; white-space: nowrap; }
  .brand-mark { width: 12px; height: 12px; background: var(--navy); flex: none; }

  /* Letterhead */
  .letterhead { position: absolute; left: 69px; top: 64px; width: 527px; height: 742px; background: var(--paper); box-shadow: 0 2px 10px rgba(0,0,0,.12); }
  .letterhead .brand { left: 45px; top: 57px; font-size: 21px; }
  .lh-address { position: absolute; right: 174px; top: 53px; text-align: right; font-family: "Roboto", sans-serif; font-size: 8px; line-height: 10.3px; color: var(--muted); font-style: normal; white-space: nowrap; }
  .lh-divider { position: absolute; left: 362px; top: 52px; width: 1px; height: 42px; background: #bbb; }
  .contact-list { list-style: none; font-family: "Roboto", sans-serif; color: var(--muted); }
  .contact-list li { display: flex; align-items: center; gap: 5px; white-space: nowrap; }
  .contact-list svg { width: 7px; height: 7px; fill: var(--navy); flex: none; }
  .lh-contacts { position: absolute; left: 372px; top: 53px; font-size: 8px; line-height: 10.3px; }
  .salutation { position: absolute; left: 46px; top: 206px; font-size: 14px; color: #444; }
  .letter-body { position: absolute; left: 46px; top: 245px; width: 438px; font-size: 8px; line-height: 11.4px; color: #555; }
  .letter-body p { margin-bottom: 11.4px; }
  .sign-off { position: absolute; left: 46px; top: 487px; font-size: 7.6px; color: #555; }
  .signature { position: absolute; left: 40px; top: 515px; width: 100px; height: 42px; background: linear-gradient(90deg, rgba(45,80,160,.12), rgba(45,80,160,.05)); }

  /* Business card */
  .business-card { position: absolute; left: 730px; top: 92px; width: 296px; height: 169px; background: var(--card); border: 1px solid #c5c9cf; }
  .business-card .brand { left: 155px; top: 24px; font-size: 17px; }
  .card-name { position: absolute; left: 155px; top: 56px; font-family: "Roboto", sans-serif; font-weight: 700; font-size: 10px; color: var(--navy-dark); }
  .card-title { position: absolute; left: 155px; top: 70px; font-family: "Roboto", sans-serif; font-size: 7.5px; color: #333; }
  .card-contacts { position: absolute; left: 155px; top: 85px; font-size: 7px; line-height: 9.6px; color: #222; }
  .card-contacts svg { fill: #222; }
  .card-footer { position: absolute; left: 0; right: 0; top: 136px; border-top: 1px solid var(--rule); padding-top: 6px; text-align: center; font-family: "Roboto", sans-serif; font-size: 7px; line-height: 10.3px; color: #333; }

  /* Envelope back */
  .envelope-back { position: absolute; left: 614px; top: 296px; width: 531px; height: 242px; background: var(--paper); box-shadow: 0 1px 6px rgba(0,0,0,.1); }
  .envelope-flap { position: absolute; left: 0; top: 0; width: 531px; height: 75px; }
  .envelope-flap path { fill: var(--navy); }
  .envelope-back .brand { left: 199px; top: 25px; font-size: 16px; color: var(--white); }
  .envelope-back .brand-mark { background: var(--white); width: 10px; height: 10px; }

  /* Envelope front */
  .envelope-front { position: absolute; left: 614px; top: 562px; width: 532px; height: 241px; background: var(--paper); box-shadow: 0 1px 6px rgba(0,0,0,.1); }
  .envelope-front .brand { left: 29px; top: 26px; font-size: 18px; }
  .env-address { position: absolute; left: 29px; top: 64px; font-family: "Roboto", sans-serif; font-size: 8px; line-height: 10.3px; color: #444; font-style: normal; }
</style>
</head>
<body>

<svg width="0" height="0" style="position:absolute">
  <defs>
    <symbol id="icon-phone" viewBox="0 0 10 10"><path d="M2 0.5 L3.6 0.5 L4.2 3 L3 3.8 Q4 6 6.2 7 L7 5.8 L9.5 6.4 L9.5 8 Q9.5 9.5 8 9.5 Q1 9 0.5 2 Q0.5 0.5 2 0.5Z"/></symbol>
    <symbol id="icon-mobile" viewBox="0 0 10 10"><path d="M2.5 0 H7.5 V10 H2.5Z M3.4 1 V8 H6.6 V1Z"/></symbol>
    <symbol id="icon-mail" viewBox="0 0 10 10"><path d="M0 2 H10 V8 H0Z M0.8 2.6 L5 5.6 L9.2 2.6Z" fill-rule="evenodd"/></symbol>
    <symbol id="icon-web" viewBox="0 0 10 10"><circle cx="5" cy="5" r="4.6"/></symbol>
  </defs>
</svg>

<section class="letterhead">
  <div class="brand"><span class="brand-mark"></span>ferngatebuild</div>
  <address class="lh-address">
    Level 3, 42 Marlow Street<br>
    Brookfield NSW 2318<br>
    National Provider Number 7291<br>
    ABN 53 219 864 317
  </address>
  <div class="lh-divider"></div>
  <ul class="contact-list lh-contacts">
    <li><svg><use href="#icon-phone"/></svg>1300 987 214</li>
    <li><svg><use href="#icon-mobile"/></svg>0432 785 619</li>
    <li><svg><use href="#icon-mail"/></svg>name@ferngatebuild.com.au</li>
    <li><svg><use href="#icon-web"/></svg>www.ferngatebuild.com.au</li>
  </ul>

  <p class="salutation">Dear Mr. Reeve,</p>
  <div class="letter-body">
    <p>Lorem ipsum dolor sit amet, consectetur adipiscing elit. Donec orci purus, luctus vitae dignissim eu, iaculis sed purus. Vivamus faucibus, ipsum nec aliquet viverra, leo mauris condimentum ligula, sit amet sagittis enim ligula quis arcu. Nam egestas tortor id nisi porttitor mattis. In tortor ante, ultricies in suscipit a, tempus non massa. Vivamus et auctor mi. Fusce vel massa nulla. Phasellus nec eros mauris, et scelerisque orci.</p>
    <p>Donec malesuada orci vitae nulla accumsan porta a id massa. Quisque accumsan iaculis magna sit amet fringilla. Maecenas consequat, magna eget tincidunt semper, odio nibh rutrum mi, id feugiat ante nisi eu risus. Vestibulum nunc orci, rhoncus a placerat in, ultricies in mi. Cras mattis varius eros, vel fringilla nisi suscipit eget. Quisque sceleris­que sagittis nulla at porttitor.</p>
    <p>Sed id augue vitae urna euismod commodo aliquet a quam. Pellentesque arcu velit, cursus et malesuada ut, con­sequat et diam. Nullam erat sem, rhoncus id ullamcorper vitae, rhoncus et arcu. In ultricies ultricies nulla, ut rutrum nisi iaculis at. Donec eu magna a metus ornare faucibus. Fusce aliquet faucibus ultricies. Morbi semper, est id tinc­idunt gravida, sem arcu adipiscing lacus, ac bibendum nulla leo eu purus. Quisque nec diam sed risus consectetur a ccumsan quis quis nibh. Vestibulum id purus lorem.</p>
    <p>It is a long established fact that a reader will be distracted by the readable content of a page when looking at its layout. The point of using Lorem Ipsum is that it has a more-or-less normal distribution of letters, as opposed to using 'Content here, content here', making it look like readable English. Many desktop publishing packages</p>
  </div>
  <p class="sign-off">Sincerely,</p>
  <div class="signature" role="img" aria-label="Handwritten signature in blue ink"></div>
</section>

<section class="business-card">
  <div class="brand"><span class="brand-mark"></span>ferngatebuild</div>
  <p class="card-name">DANIEL REEVE</p>
  <p class="card-title">CEO/FOUNDER</p>
  <ul class="contact-list card-contacts">
    <li><svg><use href="#icon-phone"/></svg>1300 987 214</li>
    <li><svg><use href="#icon-mobile"/></svg>0432 785 619</li>
    <li><svg><use href="#icon-mail"/></svg>name@ferngatebuild.com.au</li>
    <li><svg><use href="#icon-web"/></svg>www.ferngatebuild.com.au</li>
  </ul>
  <div class="card-footer">
    Level 3, 42 Marlow Street, Brookfield NSW 2318<br>
    National Provider Number 7291 | ABN 53 219 864 317
  </div>
</section>

<section class="envelope-back">
  <svg class="envelope-flap" viewBox="0 0 531 75"><path d="M0 0 H531 L524 40 Q519 75 490 75 H41 Q12 75 8 40 Z"/></svg>
  <div class="brand"><span class="brand-mark"></span>ferngatebuild</div>
</section>

<section class="envelope-front">
  <div class="brand"><span class="brand-mark"></span>ferngatebuild</div>
  <address class="env-address">
    Level 3, 42 Marlow Street<br>
    Brookfield NSW 2318<br>
    National Provider Number 7291<br>
    ABN 53 219 864 317
  </address>
</section>

</body>
</html>
```